App Design for FlavorTrek

We need an app design for a new app called FlavorTrek, which is an app designed to inspire exploration through personalized recipe generation, local restaurant discoveries, and a vibrant community platform. It caters to food enthusiasts looking to explore global cuisines or find the best local dining spots, offering a premium experience with selected features available for free.

-------UPDATED-----
This app will be AI Driven and may not be heavily dependent on media (images,videos) at first, especially for the Recipe generator feature. Our goal is to still have attractive UI. The core functionalities we are looking are the following
1. Recipe Generator: Either user choose a specific cuisine(italian,spanish), or user inputs ingredients and get recipe, or get recipe for different occasions (xmas, thanksgiving ) and get a randomly get recipe to cook, plain simple. We expect the recipes to be displayed in clear and not too generic manner starting with ingredients and expected duration at top and then step by step guide. We also intend to enable premium users to have playful action button or icon to get unlimited recipes generated until they find what they like and also have save for later feature. These premium features should be disabled for free users and prompted to subscribe if they click them with nice popup
2. Restaurant Recommendation - will have selected pictures and will be based on inputs such as zip code and other filters such as cousine types. Premium users can filter by price range, get unlimited recommendation, see actual price range in the recommendation and can save for later where they can find it later. Free users cannot filter by price (disabled) and should see it hidden in the recommendation
3. Meal Planning - will include just simple and random meal plan with just one button or limited interaction for free, users need to subscribe to get features such as customized plan such as considering allergies or diet preferences. Premium users can also get a shopping checklist of ingredients for weekly meal preps and their step by step guide for each meal recipe.
2. Community Sharing: users can view posts and engage with community content
Updates

Hello Designers,

The initial price was not fair for the work. So I have increased it. There will also be $50-100 bonus for those who come up with great designs or for those who incorporate interesting stuff. Thank you! Much appreciated 🙏

Colors
0054AA
0677BA
7BADD7
CADEEF
E8F1F8
0094D4
00A9DD
6FCCEA
C7EBF8
E9F6FB
00AB8E
00BBA5
67D7C9
C6EFE9
E9F9F6
FFC000
F8CF3A
FAE287
FDF2CF
FEFAEE
F0912C
F2A743
F7CA91
FBE8D2
FDF5EE
EE7325
F08F49
F5BC92
FAE3D3
FDF4ED
A7469A
B969AE
D3A5CF
EDDBEB
F8F0F9
6B429C
8869AF
B7A5CE
E3DAEB
F3F0F8

```html
<!DOCTYPE html>
<html lang="en">
<head>
<meta charset="utf-8">
<title>FlavorTrek – App Screens</title>
<link href="https://fonts.googleapis.com/css2?family=Plus+Jakarta+Sans:wght@400;500;600;700&display=swap" rel="stylesheet">
<style>
:root{
  --navy:#0054AA; --blue:#0677BA; --sky:#0094D4; --ice:#E8F1F8; --ice2:#E9F6FB;
  --mint:#E9F9F6; --teal:#00AB8E; --peach:#FDF5EE; --peach2:#FBE8D2; --orange:#F0912C;
  --plum-bg:#F8F0F9; --plum:#A7469A; --ink:#1B1F24; --muted:#6B7280; --line:#E3E6EA;
  --panel:#F5F6F8; --white:#fff; --disabled:#DADDE1;
}
*{box-sizing:border-box;margin:0;padding:0}
html,body{width:1200px;height:863px;overflow:hidden;background:#fff}
body{font-family:"Plus Jakarta Sans",sans-serif;color:var(--ink)}
.board{position:absolute;left:0;top:0;width:2260px;height:1625px;transform:scale(.531);transform-origin:0 0}
.section-title{position:absolute;top:52px;font-size:32px;font-weight:600;letter-spacing:-.3px}
.screen{position:absolute;top:120px;width:282px;border:2px solid var(--line);border-radius:40px;background:var(--white);overflow:hidden}
.status{position:absolute;top:14px;left:0;right:0;height:16px;font-size:12px;font-weight:600}
.status .time{position:absolute;left:44px}
.status svg{position:absolute;right:26px;top:2px}
.indicator{position:absolute;bottom:10px;left:50%;width:96px;height:3px;margin-left:-48px;border-radius:3px;background:var(--ink)}
.avatar{position:absolute;top:46px;right:16px;width:30px;height:30px;border-radius:50%;background:radial-gradient(circle at 50% 40%,#6b8f84,#2f4a48)}
.brand{position:absolute;top:285px;left:0;right:0;text-align:center;font-size:38px;font-weight:700;color:var(--blue)}
.greet{position:absolute;top:112px;width:100%;text-align:center;font-size:30px;font-weight:700}
.greet-sub{position:absolute;top:164px;width:100%;text-align:center;font-size:13px}
.feature-card{position:absolute;left:24px;top:202px;width:234px;height:110px;border-radius:14px;background:var(--ice);padding:20px 16px 0 76px}
.feature-card svg{position:absolute;left:18px;top:34px}
.feature-card h3{font-size:13px;font-weight:700;margin-bottom:6px}
.feature-card p{font-size:10.5px;line-height:1.45;color:var(--muted)}
.tiles{position:absolute;left:24px;top:334px;width:234px;display:flex;justify-content:space-between}
.tile{width:70px;text-align:center;font-size:10.5px;line-height:1.45}
.tile .box{height:58px;border-radius:12px;display:flex;align-items:center;justify-content:center;margin-bottom:8px}
.upgrade-bar{position:absolute;left:0;right:0;height:60px;border-top:1px solid #f0f1f3;background:#fff;padding:12px 18px;display:flex;align-items:center;justify-content:space-between}
.upgrade-bar p{font-size:10.5px;color:var(--muted);line-height:1.45;width:140px}
.btn-upgrade{display:flex;align-items:center;gap:5px;border:1px solid var(--sky);border-radius:16px;padding:7px 11px;font-size:11px;font-weight:700;color:var(--sky)}
.app-header{position:absolute;top:48px;left:16px;display:flex;align-items:center;gap:10px;font-size:16px;font-weight:600}
.surprise{position:absolute;left:18px;top:97px;width:246px;height:54px;border-radius:10px;background:var(--peach);padding:10px 0 0 56px}
.surprise svg{position:absolute;left:12px;top:12px}
.surprise h3{font-size:13px;font-weight:700}
.surprise p{font-size:10px;color:var(--muted);margin-top:3px}
.tabs{position:absolute;left:12px;top:166px;width:258px;display:flex;justify-content:space-between}
.tab{width:64px;text-align:center;font-size:8.5px;color:#9aa0a8;position:relative}
.tab .ic{width:30px;height:30px;border-radius:50%;background:#EEF0F2;margin:0 auto 7px;display:flex;align-items:center;justify-content:center}
.tab.active{color:var(--navy);font-weight:600}
.tab.active .ic{background:var(--navy)}
.tab .gem{position:absolute;top:-4px;right:10px;width:12px;height:12px;border-radius:50%;background:var(--sky)}
.panel{position:absolute;left:0;right:0;top:228px;bottom:0;background:var(--panel);padding:16px 14px 0}
.card{background:#fff;border-radius:12px;padding:16px 12px 14px;margin-bottom:14px}
.card h4{font-size:13px;font-weight:700;margin-bottom:14px}
.field{height:34px;border:1px solid var(--line);border-radius:17px;display:flex;align-items:center;justify-content:space-between;padding:0 4px 0 12px;font-size:12px;color:#b3b8bf;margin-top:8px}
.field .mic{width:26px;height:26px;border-radius:50%;background:#EEF0F2;display:flex;align-items:center;justify-content:center}
.chip-row{height:30px;border-radius:8px;background:#F3F4F6;display:flex;align-items:center;justify-content:space-between;padding:0 10px 0 12px;font-size:12px;margin-bottom:6px}
.btn-primary{display:block;margin:18px auto 0;width:110px;height:36px;border-radius:18px;background:var(--sky);color:#fff;font-size:12px;font-weight:700;text-align:center;line-height:36px}
.cuisines{display:grid;grid-template-columns:repeat(3,1fr);gap:6px}
.cuisine{height:29px;border:1px solid var(--line);border-radius:15px;font-size:10.5px;display:flex;align-items:center;justify-content:center}
.cuisine.on{background:var(--navy);color:#fff;border-color:var(--navy)}
.load-more{text-align:center;font-size:10px;font-weight:700;color:var(--sky);margin-top:14px}
.back-header{position:absolute;top:48px;left:16px;display:flex;gap:12px;font-size:16px;font-weight:700;line-height:1.4}
.result-top{position:absolute;left:18px;right:18px;top:118px}
.result-top .row{display:flex;justify-content:space-between;font-size:11px;color:var(--muted)}
.result-top .update{color:var(--sky);font-weight:600}
.dish-photo{margin-top:12px;height:128px;border-radius:10px;background:linear-gradient(135deg,#1e3f7a 0%,#2d4f8a 30%,#b8541f 55%,#e28a24 75%,#5a3320 100%)}
.dish-title{font-size:19px;font-weight:700;margin:16px 0 12px}
.meta{font-size:10.5px;color:var(--muted);margin-bottom:8px;display:flex;align-items:center;gap:5px}
.meta b{color:var(--ink);font-weight:600}
.result-panel{position:absolute;left:0;right:0;top:385px;bottom:0;background:var(--panel);padding:16px 14px 0}
.list li{list-style:none;display:flex;justify-content:space-between;font-size:11.5px;line-height:1.45;margin-bottom:12px;padding-left:12px;position:relative}
.list li::before{content:"";position:absolute;left:0;top:7px;width:3px;height:3px;border-radius:50%;background:#b3b8bf}
.list li span:last-child{font-size:10px;white-space:nowrap;padding-left:8px}
.list li span:first-child{max-width:175px}
.tags{display:flex;gap:6px}
.tag{background:var(--peach2);border-radius:15px;padding:7px 12px;font-size:11.5px}
.steps li{list-style:none;display:flex;gap:12px;font-size:11.5px;line-height:1.5;margin-bottom:14px}
.actions{display:flex;justify-content:space-between;margin-top:4px}
.actions div{position:relative;width:116px;height:34px;border-radius:17px;background:var(--disabled);color:#fff;font-size:11.5px;font-weight:600;text-align:center;line-height:34px}
.actions i{position:absolute;top:-6px;right:-2px;width:14px;height:14px;border-radius:50%;background:var(--sky)}
</style>
</head>
<body>
<svg width="0" height="0" style="position:absolute">
  <defs>
    <symbol id="sig" viewBox="0 0 46 12"><rect x="0" y="7" width="3" height="4" rx="1"/><rect x="4" y="5" width="3" height="6" rx="1"/><rect x="8" y="3" width="3" height="8" rx="1"/><path d="M17 5a8 8 0 0 1 10 0l-1.5 1.6a5.5 5.5 0 0 0-7 0zM19.5 8a4 4 0 0 1 5 0L22 10.6z"/><rect x="31" y="2" width="13" height="8" rx="2"/></symbol>
    <symbol id="gem" viewBox="0 0 12 12"><path d="M3 2h6l2 3-5 6-5-6z" fill="none" stroke="currentColor" stroke-width="1.2" stroke-linejoin="round"/></symbol>
    <symbol id="mic" viewBox="0 0 12 14"><rect x="4" y="1" width="4" height="8" rx="2" fill="none" stroke="#8a9099" stroke-width="1.1"/><path d="M2 7a4 4 0 0 0 8 0M6 11v2" fill="none" stroke="#8a9099" stroke-width="1.1"/></symbol>
    <symbol id="x" viewBox="0 0 14 14"><circle cx="7" cy="7" r="6" fill="none" stroke="#8a9099"/><path d="M4.8 4.8l4.4 4.4M9.2 4.8l-4.4 4.4" stroke="#8a9099"/></symbol>
    <symbol id="bowl" viewBox="0 0 30 26"><path d="M2 12h26a13 11 0 0 1-26 0z" fill="none" stroke="currentColor" stroke-width="1.8"/><path d="M8 10l2-6M15 10V2M22 10l-2-6" stroke="currentColor" stroke-width="1.8" stroke-linecap="round"/></symbol>
    <symbol id="home" viewBox="0 0 16 16"><path d="M2 7l6-5 6 5v7H2z" fill="none" stroke="#8a9099" stroke-width="1.3" stroke-linejoin="round"/></symbol>
  </defs>
</svg>

<div class="board">
  <h2 class="section-title" style="left:50px">1 of 4 : Splash Screen &amp; Landing Page</h2>
  <h2 class="section-title" style="left:732px">2 of 4 : Recipe Generator</h2>

  <!-- Splash -->
  <section class="screen" style="left:48px;height:605px">
    <div class="status"><span class="time">9:41</span><svg width="46" height="12" fill="#1B1F24"><use href="#sig"/></svg></div>
    <div class="brand">FlavorTrek</div>
    <div class="indicator"></div>
  </section>

  <!-- Landing -->
  <section class="screen" style="left:350px;height:605px">
    <div class="status"><span class="time">9:41</span><svg width="46" height="12" fill="#1B1F24"><use href="#sig"/></svg></div>
    <div class="avatar" role="img" aria-label="User profile photo"></div>
    <h1 class="greet">Hi, John</h1>
    <p class="greet-sub">What would you like today?</p>
    <div class="feature-card">
      <svg width="40" height="34" style="color:var(--navy)"><use href="#bowl"/></svg>
      <h3>Get a Recipe</h3>
      <p>Discover recipes based on ingredients, cuisine, or generate random recipe</p>
    </div>
    <div class="tiles">
      <div class="tile"><div class="box" style="background:var(--mint)"><svg width="26" height="28" viewBox="0 0 26 28" fill="none" stroke="#00AB8E" stroke-width="1.8" stroke-linecap="round"><path d="M5 2v9M2 2v6a3 3 0 0 0 6 0V2M5 11v15M19 2c-3 0-4 5-4 9h4v15"/></svg></div>Eat Out</div>
      <div class="tile"><div class="box" style="background:var(--peach)"><svg width="30" height="24" viewBox="0 0 30 24" fill="none" stroke="#F0912C" stroke-width="1.8" stroke-linecap="round"><path d="M3 18a12 12 0 0 1 24 0zM1 21h28M15 3v3"/></svg></div>Plan a Meal</div>
      <div class="tile"><div class="box" style="background:var(--plum-bg)"><svg width="28" height="28" viewBox="0 0 28 28" fill="none" stroke="#A7469A" stroke-width="1.6"><rect x="7" y="2" width="14" height="8" rx="2"/><circle cx="6" cy="17" r="2.5"/><circle cx="14" cy="17" r="2.5"/><circle cx="22" cy="17" r="2.5"/><path d="M2 26a4 4 0 0 1 8 0M10 26a4 4 0 0 1 8 0M18 26a4 4 0 0 1 8 0"/></svg></div>Engage with Community</div>
    </div>
    <div class="upgrade-bar" style="top:520px"><p>Upgrade to premium and enjoy the full features</p><span class="btn-upgrade"><svg width="12" height="12"><use href="#gem"/></svg>Upgrade</span></div>
    <div class="indicator"></div>
  </section>

  <!-- Recipe: ingredients empty -->
  <section class="screen" style="left:730px;height:605px">
    <div class="status"><span class="time">9:41</span><svg width="46" height="12" fill="#1B1F24"><use href="#sig"/></svg></div>
    <div class="app-header"><svg width="16" height="16"><use href="#home"/></svg>Recipe</div>
    <div class="avatar" role="img" aria-label="User profile photo"></div>
    <div class="surprise"><svg width="30" height="26" style="color:var(--orange)"><use href="#bowl"/></svg><h3>Surprise Me!</h3><p>Get a randomly recipe to cook</p></div>
    <div class="tabs">
      <div class="tab active"><div class="ic"><svg width="14" height="14" viewBox="0 0 14 14" fill="none" stroke="#fff" stroke-width="1.3"><rect x="2" y="5" width="10" height="7" rx="1"/><path d="M5 5V2M9 5V2"/></svg></div>Ingredients</div>
      <div class="tab"><div class="ic"><svg width="14" height="14" viewBox="0 0 14 14" fill="none" stroke="#9aa0a8" stroke-width="1.3"><path d="M3 8a3 3 0 1 1 2-5 3 3 0 0 1 4 0 3 3 0 1 1 2 5v4H3z"/></svg></div>Cuisine</div>
      <div class="tab"><div class="ic"><svg width="14" height="14" viewBox="0 0 14 14" fill="none" stroke="#9aa0a8" stroke-width="1.3"><path d="M2 12l3-8 5 5zM9 2v2M12 5h-2"/></svg></div>Occasion</div>
      <div class="tab"><i class="gem"></i><div class="ic"><svg width="14" height="14" viewBox="0 0 14 14" fill="none" stroke="#9aa0a8" stroke-width="1.3"><circle cx="7" cy="8" r="5"/><path d="M7 5v3h2"/></svg></div>Cooking Time</div>
    </div>
    <div class="panel">
      <div class="card"><h4>Add Ingredients</h4><div class="field">Add ingredient<span class="mic"><svg width="12" height="14"><use href="#mic"/></svg></span></div></div>
      <span class="btn-primary">Get a Recipe</span>
    </div>
    <div class="upgrade-bar" style="top:520px"><p>Upgrade to premium and enjoy the full features</p><span class="btn-upgrade"><svg width="12" height="12"><use href="#gem"/></svg>Upgrade</span></div>
    <div class="indicator"></div>
  </section>

  <!-- Recipe: ingredients filled -->
  <section class="screen" style="left:1032px;height:605px">
    <div class="status"><span class="time">9:41</span><svg width="46" height="12" fill="#1B1F24"><use href="#sig"/></svg></div>
    <div class="app-header"><svg width="16" height="16"><use href="#home"/></svg>Recipe</div>
    <div class="avatar" role="img" aria-label="User profile photo"></div>
    <div class="surprise"><svg width="30" height="26" style="color:var(--orange)"><use href="#bowl"/></svg><h3>Surprise Me!</h3><p>Get a randomly recipe to cook</p></div>
    <div class="tabs">
      <div class="tab active"><div class="ic"><svg width="14" height="14" viewBox="0 0 14 14" fill="none" stroke="#fff" stroke-width="1.3"><rect x="2" y="5" width="10" height="7" rx="1"/><path d="M5 5V2M9 5V2"/></svg></div>Ingredients</div>
      <div class="tab"><div class="ic"><svg width="14" height="14" viewBox="0 0 14 14" fill="none" stroke="#9aa0a8" stroke-width="1.3"><path d="M3 8a3 3 0 1 1 2-5 3 3 0 0 1 4 0 3 3 0 1 1 2 5v4H3z"/></svg></div>Cuisine</div>
      <div class="tab"><div class="ic"><svg width="14" height="14" viewBox="0 0 14 14" fill="none" stroke="#9aa0a8" stroke-width="1.3"><path d="M2 12l3-8 5 5zM9 2v2M12 5h-2"/></svg></div>Occasion</div>
      <div class="tab"><i class="gem"></i><div class="ic"><svg width="14" height="14" viewBox="0 0 14 14" fill="none" stroke="#9aa0a8" stroke-width="1.3"><circle cx="7" cy="8" r="5"/><path d="M7 5v3h2"/></svg></div>Cooking Time</div>
    </div>
    <div class="panel">
      <div class="card"><h4>Add Ingredients</h4>
        <div class="chip-row">Beef<svg width="14" height="14"><use href="#x"/></svg></div>
        <div class="chip-row">Onion<svg width="14" height="14"><use href="#x"/></svg></div>
        <div class="chip-row">Bell pepper<svg width="14" height="14"><use href="#x"/></svg></div>
        <div class="field">Add ingredient<span class="mic"><svg width="12" height="14"><use href="#mic"/></svg></span></div></div>
      <span class="btn-primary">Get a Recipe</span>
    </div>
    <div class="upgrade-bar" style="top:520px"><p>Upgrade to premium and enjoy the full features</p><span class="btn-upgrade"><svg width="12" height="12"><use href="#gem"/></svg>Upgrade</span></div>
    <div class="indicator"></div>
  </section>

  <!-- Recipe: cuisine -->
  <section class="screen" style="left:1334px;height:697px">
    <div class="status"><span class="time">9:41</span><svg width="46" height="12" fill="#1B1F24"><use href="#sig"/></svg></div>
    <div class="app-header"><svg width="16" height="16"><use href="#home"/></svg>Recipe</div>
    <div class="avatar" role="img" aria-label="User profile photo"></div>
    <div class="surprise"><svg width="30" height="26" style="color:var(--orange)"><use href="#bowl"/></svg><h3>Surprise Me!</h3><p>Get a randomly recipe to cook</p></div>
    <div class="tabs">
      <div class="tab"><div class="ic"><svg width="14" height="14" viewBox="0 0 14 14" fill="none" stroke="#9aa0a8" stroke-width="1.3"><rect x="2" y="5" width="10" height="7" rx="1"/><path d="M5 5V2M9 5V2"/></svg></div>Ingredients</div>
      <div class="tab active"><div class="ic"><svg width="14" height="14" viewBox="0 0 14 14" fill="none" stroke="#fff" stroke-width="1.3"><path d="M3 8a3 3 0 1 1 2-5 3 3 0 0 1 4 0 3 3 0 1 1 2 5v4H3z"/></svg></div>Cuisine</div>
      <div class="tab"><div class="ic"><svg width="14" height="14" viewBox="0 0 14 14" fill="none" stroke="#9aa0a8" stroke-width="1.3"><path d="M2 12l3-8 5 5zM9 2v2M12 5h-2"/></svg></div>Occasion</div>
      <div class="tab"><i class="gem"></i><div class="ic"><svg width="14" height="14" viewBox="0 0 14 14" fill="none" stroke="#9aa0a8" stroke-width="1.3"><circle cx="7" cy="8" r="5"/><path d="M7 5v3h2"/></svg></div>Cooking Time</div>
    </div>
    <div class="panel">
      <div class="card"><h4>Choose Cuisine</h4>
        <div class="cuisines"><span class="cuisine">American</span><span class="cuisine">Italian</span><span class="cuisine">Mexican</span><span class="cuisine">Japanese</span><span class="cuisine">Chinese</span><span class="cuisine">Indian</span><span class="cuisine">English</span><span class="cuisine">French</span><span class="cuisine">Korean</span></div>
        <p class="load-more">Load More</p></div>
      <div class="card"><h4>Avoided Ingredients</h4><div class="field">Add avoided ingredient<span class="mic"><svg width="12" height="14"><use href="#mic"/></svg></span></div></div>
      <span class="btn-primary">Get a Recipe</span>
    </div>
    <div class="upgrade-bar" style="top:612px"><p>Upgrade to premium and enjoy the full features</p><span class="btn-upgrade"><svg width="12" height="12"><use href="#gem"/></svg>Upgrade</span></div>
    <div class="indicator"></div>
  </section>

  <!-- Recipe: cuisine selected -->
  <section class="screen" style="left:1636px;height:766px">
    <div class="status"><span class="time">9:41</span><svg width="46" height="12" fill="#1B1F24"><use href="#sig"/></svg></div>
    <div class="app-header"><svg width="16" height="16"><use href="#home"/></svg>Recipe</div>
    <div class="avatar" role="img" aria-label="User profile photo"></div>
    <div class="surprise"><svg width="30" height="26" style="color:var(--orange)"><use href="#bowl"/></svg><h3>Surprise Me!</h3><p>Get a randomly recipe to cook</p></div>
    <div class="tabs">
      <div class="tab"><div class="ic"><svg width="14" height="14" viewBox="0 0 14 14" fill="none" stroke="#9aa0a8" stroke-width="1.3"><rect x="2" y="5" width="10" height="7" rx="1"/><path d="M5 5V2M9 5V2"/></svg></div>Ingredients</div>
      <div class="tab active"><div class="ic"><svg width="14" height="14" viewBox="0 0 14 14" fill="none" stroke="#fff" stroke-width="1.3"><path d="M3 8a3 3 0 1 1 2-5 3 3 0 0 1 4 0 3 3 0 1 1 2 5v4H3z"/></svg></div>Cuisine</div>
      <div class="tab"><div class="ic"><svg width="14" height="14" viewBox="0 0 14 14" fill="none" stroke="#9aa0a8" stroke-width="1.3"><path d="M2 12l3-8 5 5zM9 2v2M12 5h-2"/></svg></div>Occasion</div>
      <div class="tab"><i class="gem"></i><div class="ic"><svg width="14" height="14" viewBox="0 0 14 14" fill="none" stroke="#9aa0a8" stroke-width="1.3"><circle cx="7" cy="8" r="5"/><path d="M7 5v3h2"/></svg></div>Cooking Time</div>
    </div>
    <div class="panel">
      <div class="card"><h4>Choose Cuisine</h4>
        <div class="cuisines"><span class="cuisine">American</span><span class="cuisine">Italian</span><span class="cuisine on">Mexican</span><span class="cuisine">Japanese</span><span class="cuisine">Chinese</span><span class="cuisine">Indian</span><span class="cuisine">English</span><span class="cuisine">French</span><span class="cuisine">Korean</span></div>
        <p class="load-more">Load More</p></div>
      <div class="card"><h4>Avoided Ingredients</h4>
        <div class="chip-row">Cardnamon<svg width="14" height="14"><use href="#x"/></svg></div>
        <div class="chip-row">Cinnamon<svg width="14" height="14"><use href="#x"/></svg></div>
        <div class="field">Add avoided ingredient<span class="mic"><svg width="12" height="14"><use href="#mic"/></svg></span></div></div>
      <span class="btn-primary">Get a Recipe</span>
    </div>
    <div class="upgrade-bar" style="top:681px"><p>Upgrade to premium and enjoy the full features</p><span class="btn-upgrade"><svg width="12" height="12"><use href="#gem"/></svg>Upgrade</span></div>
    <div class="indicator"></div>
  </section>

  <!-- Recommended recipe -->
  <section class="screen" style="left:1938px;height:1463px">
    <div class="status"><span class="time">9:41</span><svg width="46" height="12" fill="#1B1F24"><use href="#sig"/></svg></div>
    <div class="back-header"><svg width="16" height="16" viewBox="0 0 16 16" fill="none" stroke="#8a9099" stroke-width="1.4" style="margin-top:4px"><path d="M14 8H2M7 3L2 8l5 5"/></svg><span>Recommended<br>Recipe</span></div>
    <div class="avatar" role="img" aria-label="User profile photo"></div>
    <div class="result-top">
      <div class="row"><span>Your recipe is here :</span><span class="update">⟳ Update</span></div>
      <div class="dish-photo" role="img" aria-label="Photo of beef stir-fry with peppers in a blue bowl"></div>
      <h2 class="dish-title">Mexican Beef Stir-Fry</h2>
      <p class="meta">◌ Cuisine: <b>Mexican</b></p>
      <p class="meta">◷ Ready in: <b>27 minutes</b></p>
    </div>
    <div class="result-panel">
      <div class="card"><h4>Your Ingredients</h4><ul class="list">
        <li><span>Beef</span><span>16 oz</span></li>
        <li><span>Onion, cut into thin wedges</span><span>1</span></li>
        <li style="margin-bottom:0"><span>Bell pepper, cut into strips</span><span>1</span></li></ul></div>
      <div class="card"><h4>More Ingredients</h4><ul class="list">
        <li><span>Vegetable oil</span><span>1 tsp</span></li>
        <li><span>Garlic clove, minced</span><span>1</span></li>
        <li><span>Ground cumin</span><span>1 tsp</span></li>
        <li><span>Dried oregano</span><span>1 tsp</span></li>
        <li><span>Jalapeno pepper, seeded and cut into strips</span><span>1-2</span></li>
        <li style="margin-bottom:0"><span>Iceberg lettuce, shredded</span><span>3 cups</span></li></ul></div>
      <div class="card"><h4>Avoided Ingredients</h4><div class="tags"><span class="tag">Cardnamon</span><span class="tag">Cinnamon</span></div></div>
      <div class="card"><h4>Directions</h4><ol class="steps">
        <li><span>1.</span><span>Trim excess fat from the beef; slice steak diagonally across the grain into 1/8 inch strips. Set aside.</span></li>
        <li><span>2.</span><span>Combine oil, garlic, cumin, and oregano; stir well. Heat half of oil mixture in a large nonstick skillet over medium-high heat for 2 minutes. Add onion, red pepper, and jalapeno pepper, and stir-fry 2 minutes, or until crisp-tender. Remove vegetables from the skillet; set aside, and keep warm.</span></li>
        <li style="margin-bottom:0"><span>3.</span><span>Add remaining oil mixture to the skillet. Add the reserved beef strips, and stir-fry 2 minutes. Return vegetables to the skillet and stir-fry until thoroughly heated. Serve over lettuce, and garnish if desired.</span></li></ol></div>
      <div class="actions"><div>Get New!<i></i></div><div>Save For Later<i></i></div></div>
    </div>
    <div class="upgrade-bar" style="top:1378px"><p>Upgrade to premium and enjoy the full features</p><span class="btn-upgrade"><svg width="12" height="12"><use href="#gem"/></svg>Upgrade</span></div>
    <div class="indicator"></div>
  </section>
</div>
</body>
</html>
```